I need a two page flyer (one page front and back) outlining our residential furniture rental options.

Title: Premium Residential Furniture Rentals

GOOD
Our Bellmore Ridge Furniture Package is designed to offer a perfect balance of affordability and style, without compromising on quality. This package features a selection of functional and aesthetically pleasing furniture pieces, ideal for those looking to create a polished and professional space. With quick installation handled by our experienced in-house team, you can expect a smooth and hassle-free setup. This package ensures both convenience and value, providing a streamlined solution for your needs.
Living room, dining room and bedroom (additional bedrooms available)
- $710/month with a 3 month commitment
- $570/month with a 6 month commitment

BETTER
Our Premium Furniture Package takes comfort and style to the next level, offering an enhanced experience compared to our Bellmore option. Carefully selected with durability in mind, this package features high-quality, convenient furniture designed for both functionality and aesthetics. Perfect for those seeking a more refined look and superior comfort, it’s ideal for creating a sophisticated and inviting environment. With attention to detail in both design and craftsmanship, the premium package elevates any space, ensuring a higher standard of comfort and style that caters to both employees and clients.
- $1,150/month with a 3 month commitment
- $900/month with a 6 month commitment

BEST
Our Custom Furniture Package offers a tailored experience where you’ll work directly with our expert designer to create the ultimate luxurious and functional space. We include lounging, dining, sleeping and working from home, this package allows you to curate a space that perfectly fits your needs and style. With personalized attention to detail, we ensure every element is designed to provide the highest level of comfort, convenience, and elegance, transforming your space into a sophisticated sanctuary for relaxation and enjoyment.
Please inquire for pricing

www.quillbyhomeleasing.example

```html
<!DOCTYPE html>
<html lang="en">
<head>
<meta charset="utf-8">
<title>Premium Residential Furniture Rentals</title>
<link href="https://fonts.googleapis.com/css2?family=Great+Vibes&family=Raleway:ital,wght@0,300;0,400;0,500;0,700;1,400&display=swap" rel="stylesheet">
<style>
:root{
  --backdrop:#c8c8ca;
  --ink-dark:#141517;
  --paper:#ffffff;
  --navy:#2e3192;
  --navy-deep:#22246c;
  --gold:#f2c230;
  --text-light:#e8e8ea;
  --text-dark:#2b2c5e;
  --line:#9a9aa0;
}
*{margin:0;padding:0;box-sizing:border-box}
html,body{width:1200px;height:777px;overflow:hidden;background:var(--backdrop)}
body{position:relative;font-family:"Raleway",sans-serif}
.page{position:absolute;top:48px;width:521px;height:674px;background:var(--ink-dark);overflow:hidden}
.page--front{left:57px}
.page--back{left:626px}
.abs{position:absolute}
.front-top{left:0;top:0;width:521px;height:296px;background:var(--paper)}

.brand-name{font-weight:400;font-size:14px;letter-spacing:.5px;line-height:1.2;text-transform:uppercase;white-space:nowrap}
.brand-name--front{left:39px;top:42px;color:var(--text-dark)}
.brand-name--back{left:314px;top:598px;color:var(--text-light)}

.title{left:266px;top:27px;font-weight:400;font-size:20px;line-height:23px;color:var(--text-dark);letter-spacing:.2px}

.photo-frame{left:33px;top:100px;width:455px;height:257px;background:var(--paper);padding:3px 5px 5px}
.photo{width:100%;height:100%}
.photo--apartment{background:linear-gradient(120deg,#8a6a4a 0%,#d9d4cc 35%,#eceae6 60%,#6d6a66 100%)}
.photo--bedroom-set{background:linear-gradient(180deg,#f6f6f6 0%,#bdbdbd 55%,#5b5b5e 100%)}
.photo--living{background:linear-gradient(135deg,#e7e3dc 0%,#c9bca7 45%,#7a7470 80%,#3a3a3c 100%)}
.photo--great-room{background:linear-gradient(100deg,#a9865e 0%,#efe6c8 30%,#c9c2b6 60%,#4f6f4a 100%)}

.tier{font-family:"Great Vibes",cursive;color:var(--gold);font-weight:400;line-height:1}
.tier--good{left:48px;top:367px;font-size:60px}
.tier--better{left:49px;top:18px;font-size:60px}
.tier--best{left:49px;top:302px;font-size:60px}

.copy{font-weight:300;color:var(--text-light);font-size:10px;line-height:11.2px}
.copy--good{left:241px;top:420px;width:252px}
.copy--better{left:242px;top:65px;width:252px}
.copy--best{left:37px;top:507px;width:448px}
.inquire{left:37px;top:576px;font-weight:700;font-size:11px;color:#fff}

.price{display:flex;width:191px;height:17px;background:var(--navy);color:#fff;align-items:center}
.price__amount{background:var(--navy-deep);height:100%;width:72px;padding-left:6px;font-weight:700;font-size:10px;display:flex;align-items:center;clip-path:polygon(0 0,90% 0,100% 50%,90% 100%,0 100%)}
.price__term{font-size:7.6px;font-weight:500;padding-left:6px}

.rooms{width:220px;height:72px}
.room{position:absolute;top:0;width:80px;text-align:center;color:var(--text-light);font-weight:300;font-size:9px}
.room svg{display:block;margin:0 auto 8px}
.room-divider{position:absolute;top:2px;height:42px;border-left:1px dotted #8a8a90}
.rooms__note{position:absolute;left:0;top:68px;width:220px;text-align:center;font-style:italic;font-size:10px;color:var(--text-light)}

.footer{left:0;top:641px;width:521px;display:flex;align-items:center;gap:8px}
.footer__rule{flex:1;border-top:1px solid var(--line)}
.footer__url{font-size:13px;font-weight:300;color:#fff;letter-spacing:.2px}
.footer__url b{font-weight:500}
</style>
</head>
<body>

<section class="page page--front">
  <div class="abs front-top"></div>

  <p class="abs brand-name brand-name--front">Quillby Home Leasing</p>

  <h1 class="abs title">PREMIUM RESIDENTIAL<br>FURNITURE RENTALS</h1>

  <div class="abs photo-frame">
    <div class="photo photo--apartment" role="img" aria-label="Furnished open-plan apartment with kitchen, dining stools, living area and bedroom"></div>
  </div>

  <h2 class="abs tier tier--good">Good</h2>
  <div class="abs photo--bedroom-set" style="left:36px;top:424px;width:188px;height:95px" role="img" aria-label="Bedroom furniture set with tufted bed, nightstand and dresser"></div>

  <p class="abs copy copy--good">Our Bellmore Ridge Furniture Package is designed to offer a perfect balance of affordability and style, without compromising on quality. This package features a selection of functional and aesthetically pleasing furniture pieces, ideal for those looking to create a polished and professional space. With quick installation handled by our experienced in-house team, you can expect a smooth and hassle-free setup. This package ensures both convenience and value, providing a streamlined solution for your needs.</p>

  <div class="abs price" style="left:35px;top:532px"><span class="price__amount">$710/month</span><span class="price__term">with a 3 month commitment</span></div>
  <div class="abs price" style="left:35px;top:553px"><span class="price__amount">$570/month</span><span class="price__term">with a 6 month commitment</span></div>

  <div class="abs rooms" style="left:245px;top:542px">
    <div class="room" style="left:-18px">
      <svg width="38" height="38" viewBox="0 0 38 38" fill="none" stroke="#fff" stroke-width="1"><circle cx="19" cy="19" r="18.5"/><path d="M11 26v-6h16v6M13 20v-3h12v3M11 26h16M12 12h4l-1 3h-2zM14 15v11"/></svg>
      Living room
    </div>
    <div class="room-divider" style="left:64px"></div>
    <div class="room" style="left:70px">
      <svg width="38" height="38" viewBox="0 0 38 38" fill="none" stroke="#fff" stroke-width="1"><circle cx="19" cy="19" r="18.5"/><path d="M14 10h10v6H14zM11 20h16M13 20v7M25 20v7M10 17v10M28 17v10M10 23h3M25 23h3"/></svg>
      dining room and
    </div>
    <div class="room-divider" style="left:158px"></div>
    <div class="room" style="left:151px">
      <svg width="38" height="38" viewBox="0 0 38 38" fill="none" stroke="#fff" stroke-width="1"><circle cx="19" cy="19" r="18.5"/><path d="M14 10h10v5H14zM10 24v-7h18v7M10 21h18M10 24v3M28 24v3M13 17v-2h5v2M20 17v-2h5v2"/></svg>
      bedroom
    </div>
    <p class="rooms__note">(additional bedrooms available)</p>
  </div>

  <footer class="abs footer">
    <span class="footer__rule"></span>
    <span class="footer__url">www.<b>quillbyhomeleasing</b>.example</span>
    <span class="footer__rule"></span>
  </footer>
</section>

<section class="page page--back">
  <h2 class="abs tier tier--better">Better</h2>
  <div class="abs photo--living" style="left:37px;top:69px;width:189px;height:172px" role="img" aria-label="Living room with beige tufted sofa, armchair, abstract wall art and round coffee table"></div>

  <p class="abs copy copy--better">Our Premium Furniture Package takes comfort and style to the next level, offering an enhanced experience compared to our Bellmore option. Carefully selected with durability in mind, this package features high-quality, convenient furniture designed for both functionality and aesthetics. Perfect for those seeking a more refined look and superior comfort, it’s ideal for creating a sophisticated and inviting environment. With attention to detail in both design and craftsmanship, the premium package elevates any space, ensuring a higher standard of comfort and style that caters to both employees and clients.</p>

  <div class="abs price" style="left:37px;top:251px"><span class="price__amount">$1,150/month</span><span class="price__term">with a 3 month commitment</span></div>
  <div class="abs price" style="left:37px;top:272px"><span class="price__amount">$900/month</span><span class="price__term">with a 6 month commitment</span></div>

  <div class="abs rooms" style="left:246px;top:203px">
    <div class="room" style="left:-18px">
      <svg width="38" height="38" viewBox="0 0 38 38" fill="none" stroke="#fff" stroke-width="1"><circle cx="19" cy="19" r="18.5"/><path d="M11 26v-6h16v6M13 20v-3h12v3M11 26h16M12 12h4l-1 3h-2zM14 15v11"/></svg>
      Living room
    </div>
    <div class="room-divider" style="left:64px"></div>
    <div class="room" style="left:70px">
      <svg width="38" height="38" viewBox="0 0 38 38" fill="none" stroke="#fff" stroke-width="1"><circle cx="19" cy="19" r="18.5"/><path d="M14 10h10v6H14zM11 20h16M13 20v7M25 20v7M10 17v10M28 17v10M10 23h3M25 23h3"/></svg>
      dining room and
    </div>
    <div class="room-divider" style="left:159px"></div>
    <div class="room" style="left:151px">
      <svg width="38" height="38" viewBox="0 0 38 38" fill="none" stroke="#fff" stroke-width="1"><circle cx="19" cy="19" r="18.5"/><path d="M14 10h10v5H14zM10 24v-7h18v7M10 21h18M10 24v3M28 24v3M13 17v-2h5v2M20 17v-2h5v2"/></svg>
      bedroom
    </div>
    <p class="rooms__note">(additional bedrooms available)</p>
  </div>

  <h2 class="abs tier tier--best">Best</h2>
  <div class="abs photo--great-room" style="left:37px;top:354px;width:449px;height:143px" role="img" aria-label="Spacious great room with sectional sofa, navy armchairs, fireplace and lit built-in shelving"></div>

  <p class="abs copy copy--best">Our Custom Furniture Package offers a tailored experience where you’ll work directly with our expert designer to create the ultimate luxurious and functional space. We include lounging, dining, sleeping and working from home, this package allows you to curate a space that perfectly fits your needs and style. With personalized attention to detail, we ensure every element is designed to provide the highest level of comfort, convenience, and elegance, transforming your space into a sophisticated sanctuary for relaxation and enjoyment.</p>
  <p class="abs inquire">Please inquire for pricing</p>

  <p class="abs brand-name brand-name--back">Quillby Home Leasing</p>

  <footer class="abs footer">
    <span class="footer__rule"></span>
    <span class="footer__url">www.<b>quillbyhomeleasing</b>.example</span>
    <span class="footer__rule"></span>
  </footer>
</section>

</body>
</html>
```